Revamp QuillStoneKit.com

https://quillstonekit.com/ needs a revamp. We like the general style and colors of the site, we just want to modernize the landing page, product page, view cart page, and the final confirm page.

I'm just looking for the PSD (Photoshop files) as the deliverable.

Quick Summary
Please redesign the following Pages:
1) https://quillstonekit.com/
2) https://quillstonekit.com/rubberTracks/QuillStoneKit/400x725nx70.php (product Page)
3) https://quillstonekit.com/viewCart.php (view cart - Add something to cart to see)
4) https://quillstonekit.com/confirmShoppingCart.php (confirm cart - Add something to cart to see)

```html
<!DOCTYPE html>
<html lang="en">
<head>
<meta charset="utf-8">
<title>QuillStoneKit – Rubber Tracks</title>
<link href="https://fonts.googleapis.com/css2?family=Oswald:wght@400;500;600;700&family=Lato:wght@400;700&family=Merriweather:wght@400&display=swap" rel="stylesheet">
<style>
:root{
  --cream:#f5f0e4;
  --ink:#231f1c;
  --dark:#1d1d1d;
  --bar:#3b3b3b;
  --gold:#c9a650;
  --card:#d9c188;
  --accent:#ef5a3e;
  --accent-soft:#f6c3b1;
  --line:#efb9a5;
  --tread:#5b5956;
  --footer:#2b2b2b;
  --muted:#b9b2a4;
}
*{box-sizing:border-box;margin:0;padding:0}
html,body{width:1200px;height:3863px;overflow:hidden}
body{position:relative;background:var(--cream);font-family:'Lato',sans-serif;color:var(--ink)}
.abs{position:absolute}

/* header */
.site-header{left:0;top:0;width:1200px;height:157px;background:var(--cream)}
.brand{left:70px;top:72px;font-family:'Oswald',sans-serif;font-weight:700;font-size:34px;line-height:40px;color:var(--ink);display:flex;align-items:center;gap:10px}
.brand .mark{width:18px;height:18px;background:var(--ink)}
.util{top:10px;font-family:'Oswald',sans-serif;font-size:19px;line-height:34px;color:var(--gold);display:flex;align-items:center;gap:10px;text-transform:uppercase}
.util svg{width:36px;height:30px}
.nav{top:74px;left:680px;display:flex;gap:24px;font-family:'Oswald',sans-serif;font-weight:500;font-size:24px;line-height:36px;text-transform:uppercase}
.nav a{color:var(--ink);text-decoration:none}
.nav a.active{color:var(--accent)}
.search-icon{left:1092px;top:76px}

/* hero */
.hero{left:0;top:157px;width:1200px;height:513px;background:var(--dark);overflow:hidden}
.hero-photo{position:absolute;inset:0;background:linear-gradient(120deg,#4a4640 0%,#7d7366 40%,#b79a45 70%,#6a6254 100%);clip-path:polygon(690px 0,1200px 0,1200px 513px,570px 513px)}
.hero-kicker{left:214px;top:86px;font-family:'Oswald',sans-serif;font-size:20px;line-height:26px;color:#8d8d8d;text-transform:uppercase;letter-spacing:.5px}
.hero-title{left:95px;top:114px;font-family:'Oswald',sans-serif;font-weight:700;font-size:64px;color:#fff;line-height:74px}
.hero-sub{left:328px;top:198px;font-family:'Oswald',sans-serif;font-weight:600;font-size:22px;line-height:30px;color:var(--gold);letter-spacing:4px}
.hero-text{left:93px;top:250px;width:420px;font-family:'Merriweather',serif;font-size:12px;line-height:20px;color:#f0f0f0}
.buy{left:95px;top:360px;width:155px;height:44px;background:#fff;border-left:6px solid var(--gold);clip-path:polygon(0 0,86% 0,100% 50%,86% 100%,0 100%);font-family:'Oswald',sans-serif;font-size:22px;line-height:44px;color:var(--ink);padding-left:30px;text-transform:uppercase}

/* section heads */
.section-head{left:0;width:1200px;text-align:center}
.kicker{font-family:'Oswald',sans-serif;font-size:27px;line-height:34px;letter-spacing:6px;color:var(--accent);text-transform:uppercase}
.title{font-family:'Oswald',sans-serif;font-weight:600;font-size:52px;color:var(--ink);text-transform:uppercase;line-height:1.2}
.title .dot{font-size:30px;vertical-align:middle;margin:0 22px}
.tread{background:var(--tread);height:88px;width:170px}
.tread.r{left:1054px;width:146px}
.tread.l{left:0}

/* carousel */
.cat-card{top:885px;width:225px;height:298px;border:2px solid var(--line);background:var(--cream);text-align:center}
.cat-card.featured{background:var(--accent-soft)}
.cat-card .pic{position:absolute;left:22px;top:22px;width:181px;height:120px;border-radius:6px}
.cat-card h3{position:absolute;left:0;right:0;top:168px;font-family:'Oswald',sans-serif;font-weight:500;font-size:27px;line-height:32px;color:var(--ink);text-transform:uppercase}
.cat-card .btn{position:absolute;left:48px;top:240px;width:130px;height:32px;background:var(--accent);color:#fff;font-family:'Oswald',sans-serif;font-size:16px;line-height:32px;text-transform:uppercase}
.chev{top:1004px}

/* product grid */
.prod{width:309px;height:572px;background:var(--card)}
.prod .tag{position:absolute;left:0;top:0;width:118px;height:27px;background:var(--accent);color:#fff;font-family:'Oswald',sans-serif;font-size:14px;line-height:27px;padding-left:30px;text-transform:uppercase}
.prod .rating{position:absolute;right:8px;top:5px;font-size:12px;line-height:18px;color:#6a5a35;display:flex;align-items:center;gap:8px}
.prod .stars{color:#fff6dd;letter-spacing:1px;font-size:14px}
.prod .pic{position:absolute;left:64px;top:58px;width:180px;height:188px;background:linear-gradient(160deg,#3a3a3a,#111);border-radius:40px}
.prod .thumbs{position:absolute;left:48px;top:263px;display:flex;gap:21px}
.prod .thumbs span{width:63px;height:62px;background:#f4efe4;position:relative}
.prod .thumbs span::after{content:"";position:absolute;left:16px;top:14px;width:31px;height:34px;background:#1d1d1d;border-radius:8px}
.prod .name{position:absolute;left:0;right:0;top:320px;text-align:center;font-size:31px;line-height:38px;color:var(--ink)}
.prod .price{position:absolute;left:0;right:14px;top:408px;text-align:center;font-size:54px;line-height:64px;color:var(--accent)}
.prod .note{position:absolute;left:0;right:20px;top:490px;text-align:center;font-size:10px;line-height:14px;color:var(--accent)}
.prod .shop{position:absolute;left:0;bottom:0;width:309px;height:62px;background:var(--bar);color:#fff;text-align:center;font-family:'Oswald',sans-serif;font-size:21px;line-height:62px;text-transform:uppercase}

/* brands */
.brand-tile{width:213px;height:117px;background:#fff;text-align:center}
.brand-tile .name{margin-top:30px;font-family:'Oswald',sans-serif;font-weight:700;font-size:38px;line-height:40px;text-transform:uppercase}
.brand-tile .cap{margin-top:8px;font-size:11px;line-height:14px;color:#444}
.c-gold{color:#f0b21d}.c-red{color:#d8202b}.c-ink{color:#1d1d1d}

/* footer */
.footer-band{left:0;top:3408px;width:1200px;height:69px;background:linear-gradient(180deg,#6a6865,#3f3d3b)}
.site-footer{left:0;top:3477px;width:1200px;height:386px;background:var(--footer);color:#fff}
.foot-brand{left:33px;top:100px;font-family:'Oswald',sans-serif;font-weight:700;font-size:62px;line-height:76px;color:#fff}
.foot-h{font-family:'Oswald',sans-serif;font-weight:500;font-size:32px;line-height:42px}
.links{left:550px;top:138px;list-style:none;font-family:'Oswald',sans-serif;font-size:18px;line-height:38px}
.search{left:780px;top:121px;width:369px;height:38px;display:flex}
.search .field{flex:1;background:#fff;color:#888;font-size:15px;line-height:20px;padding:9px 16px;white-space:nowrap;overflow:hidden}
.search .go{width:46px;background:var(--gold);display:flex;align-items:center;justify-content:center}
.social{top:199px;width:57px;height:57px;background:#4a4a4a}
.social.primary{background:var(--accent)}
.safe{left:92px;top:243px;font-family:'Oswald',sans-serif;font-size:17px;line-height:24px;display:flex;gap:30px}
.payments{left:100px;top:276px;display:flex;gap:8px}
.payments span{width:36px;height:24px;background:#dcdcdc;border-radius:3px}
.payments span.wide{width:106px;background:#111;border:1px solid #666}
.lock{left:58px;top:268px}
.copyright{left:0;top:3834px;width:1200px;text-align:center;font-size:15px;line-height:20px;color:var(--muted)}
</style>
</head>
<body>

<header class="abs site-header">
  <div class="abs brand"><span class="mark"></span>QuillStoneKit</div>
  <div class="abs util" style="left:606px">
    <svg viewBox="0 0 36 30"><rect x="1" y="1" width="34" height="28" rx="3" fill="#e9dcb8"/><path d="M8 9h4l3 9h10l2-6H13" fill="none" stroke="#c9a650" stroke-width="2"/><circle cx="16" cy="22" r="1.8" fill="#c9a650"/><circle cx="24" cy="22" r="1.8" fill="#c9a650"/></svg>
    Checkout (0)
  </div>
  <div class="abs util" style="left:847px">
    <svg viewBox="0 0 36 30"><rect x="1" y="1" width="34" height="28" rx="3" fill="#e9dcb8"/><rect x="8" y="8" width="20" height="14" fill="none" stroke="#c9a650" stroke-width="2"/><path d="M8 8l10 8 10-8" fill="none" stroke="#c9a650" stroke-width="2"/></svg>
    support@quillstonekit.com
  </div>
  <nav class="abs nav"><a class="active">Home</a><a>Products</a><a>About</a><a>Conatct</a></nav>
  <svg class="abs search-icon" width="30" height="30" viewBox="0 0 30 30"><circle cx="12" cy="12" r="9" fill="none" stroke="#231f1c" stroke-width="3"/><path d="M19 19l8 8" stroke="#231f1c" stroke-width="3.5" stroke-linecap="round"/></svg>
</header>

<section class="abs hero">
  <div class="hero-photo" role="img" aria-label="Close-up photo of a yellow compact excavator's rubber track on pavement"></div>
  <div class="abs hero-kicker">Comfortable Reliability</div>
  <div class="abs hero-title">QUILLSTONEKIT</div>
  <div class="abs hero-sub">TRACKS</div>
  <p class="abs hero-text">Lorem Ipsum is simply dummy text of the printing and typesetting industry. Lorem Ipsum has been the industry's standard dummy text ever since the 1500s, when an unknown printer took a galley of type and scrambled it to make a type specimen book.</p>
  <div class="abs buy">Buy Now</div>
</section>

<!-- products carousel -->
<div class="abs tread l" style="top:738px" role="img" aria-label="Tire tread pattern"></div>
<div class="abs tread r" style="top:738px" role="img" aria-label="Tire tread pattern"></div>
<div class="abs section-head" style="top:726px">
  <div class="kicker">Shop</div>
  <div class="title"><span class="dot">•</span>Our Products<span class="dot">•</span></div>
</div>

<svg class="abs chev" style="left:78px" width="30" height="50" viewBox="0 0 30 50"><path d="M26 3L5 25l21 22" fill="none" stroke="#c9a650" stroke-width="4"/></svg>
<svg class="abs chev" style="left:1080px" width="30" height="50" viewBox="0 0 30 50"><path d="M4 3l21 22L4 47" fill="none" stroke="#c9a650" stroke-width="4"/></svg>

<div class="abs cat-card" style="left:212px">
  <div class="pic" role="img" aria-label="Yellow tracked dumper" style="background:linear-gradient(135deg,#f3e34a,#3a3a3a)"></div>
  <h3>Dumper Rubber<br>Tracks</h3><div class="btn">Shop Now</div>
</div>
<div class="abs cat-card featured" style="left:492px">
  <div class="pic" role="img" aria-label="Red mini digger" style="background:linear-gradient(135deg,#d8322a,#2b2b2b)"></div>
  <h3>Mini Digger<br>Tracks</h3><div class="btn">Shop Now</div>
</div>
<div class="abs cat-card" style="left:764px">
  <div class="pic" role="img" aria-label="Skid steer with mulcher attachment" style="background:linear-gradient(135deg,#2e2e2e,#d4b43a)"></div>
  <h3>Skid Steer<br>Tracks</h3><div class="btn">Shop Now</div>
</div>

<!-- product grid -->
<div class="abs tread l" style="top:1344px" role="img" aria-label="Tire tread pattern"></div>
<div class="abs tread r" style="top:1344px" role="img" aria-label="Tire tread pattern"></div>
<div class="abs section-head" style="top:1322px">
  <div class="kicker">Discover</div>
  <div class="title"><span class="dot">•</span>Farm Tough Rubber Tracks<span class="dot">•</span></div>
</div>

<article class="abs prod" style="left:78px;top:1533px"><div class="tag">In Stock</div><div class="rating"><span class="stars">★★★★★</span>8 Reviews</div><div class="pic" role="img" aria-label="Black rubber track"></div><div class="thumbs"><span></span><span></span><span></span></div><div class="name">RUBBER TRACK<br>180x72x39</div><div class="price">$109.89</div><div class="note">FREE Shipping - Tax Incl.</div><div class="shop">Shop Now</div></article>
<article class="abs prod" style="left:440px;top:1533px"><div class="tag">In Stock</div><div class="rating"><span class="stars">★★★★★</span>8 Reviews</div><div class="pic" role="img" aria-label="Black rubber track"></div><div class="thumbs"><span></span><span></span><span></span></div><div class="name">RUBBER TRACK<br>180x72x39</div><div class="price">$109.89</div><div class="note">FREE Shipping - Tax Incl.</div><div class="shop">Shop Now</div></article>
<article class="abs prod" style="left:800px;top:1533px"><div class="tag">In Stock</div><div class="rating"><span class="stars">★★★★★</span>8 Reviews</div><div class="pic" role="img" aria-label="Black rubber track"></div><div class="thumbs"><span></span><span></span><span></span></div><div class="name">RUBBER TRACK<br>180x72x39</div><div class="price">$109.89</div><div class="note">FREE Shipping - Tax Incl.</div><div class="shop">Shop Now</div></article>
<article class="abs prod" style="left:79px;top:2157px"><div class="tag">In Stock</div><div class="rating"><span class="stars">★★★★★</span>8 Reviews</div><div class="pic" role="img" aria-label="Black rubber track"></div><div class="thumbs"><span></span><span></span><span></span></div><div class="name">RUBBER TRACK<br>180x72x39</div><div class="price">$109.89</div><div class="note">FREE Shipping - Tax Incl.</div><div class="shop">Shop Now</div></article>
<article class="abs prod" style="left:441px;top:2157px"><div class="tag">In Stock</div><div class="rating"><span class="stars">★★★★★</span>8 Reviews</div><div class="pic" role="img" aria-label="Black rubber track"></div><div class="thumbs"><span></span><span></span><span></span></div><div class="name">RUBBER TRACK<br>180x72x39</div><div class="price">$109.89</div><div class="note">FREE Shipping - Tax Incl.</div><div class="shop">Shop Now</div></article>
<article class="abs prod" style="left:801px;top:2157px"><div class="tag">In Stock</div><div class="rating"><span class="stars">★★★★★</span>8 Reviews</div><div class="pic" role="img" aria-label="Black rubber track"></div><div class="thumbs"><span></span><span></span><span></span></div><div class="name">RUBBER TRACK<br>180x72x39</div><div class="price">$109.89</div><div class="note">FREE Shipping - Tax Incl.</div><div class="shop">Shop Now</div></article>

<!-- brands -->
<div class="abs tread l" style="top:2812px" role="img" aria-label="Tire tread pattern"></div>
<div class="abs tread r" style="top:2812px" role="img" aria-label="Tire tread pattern"></div>
<div class="abs section-head" style="top:2810px">
  <div class="kicker">Shop</div>
  <div class="title"><span class="dot">•</span>Tracks by Brand<span class="dot">•</span></div>
</div>

<div class="abs brand-tile" style="left:104px;top:2994px"><div class="name c-gold">Harlan</div><div class="cap">Harlan® Replacement Tracks</div></div>
<div class="abs brand-tile" style="left:357px;top:2994px"><div class="name c-red">Vantor</div><div class="cap">Vantor® Replacement Tracks</div></div>
<div class="abs brand-tile" style="left:612px;top:2994px"><div class="name c-ink">Trenchly</div><div class="cap">Trenchly® Replacement Tracks</div></div>
<div class="abs brand-tile" style="left:858px;top:2994px"><div class="name c-ink">Kestrel</div><div class="cap">Kestrel® Replacement Tracks</div></div>
<div class="abs brand-tile" style="left:100px;top:3177px"><div class="name c-gold">Harlan</div><div class="cap">Harlan® Replacement Tracks</div></div>
<div class="abs brand-tile" style="left:353px;top:3177px"><div class="name c-red">Vantor</div><div class="cap">Vantor® Replacement Tracks</div></div>
<div class="abs brand-tile" style="left:608px;top:3177px"><div class="name c-ink">Trenchly</div><div class="cap">Trenchly® Replacement Tracks</div></div>
<div class="abs brand-tile" style="left:855px;top:3177px"><div class="name c-ink">Kestrel</div><div class="cap">Kestrel® Replacement Tracks</div></div>

<!-- footer -->
<div class="abs footer-band" role="img" aria-label="Tire tread pattern band"></div>
<footer class="abs site-footer">
  <div class="abs foot-brand">QuillStoneKit</div>
  <div class="abs foot-h" style="left:550px;top:66px">Quick Links</div>
  <ul class="abs links"><li>Home</li><li>About</li><li>Contact Us</li></ul>
  <div class="abs foot-h" style="left:876px;top:64px">Search Tracks</div>
  <div class="abs search"><div class="field">Kestrel 325 Or 300x52.5x82</div><div class="go"><svg width="24" height="24" viewBox="0 0 24 24"><circle cx="10" cy="10" r="7" fill="none" stroke="#1d1d1d" stroke-width="2.5"/><path d="M15 15l6 6" stroke="#1d1d1d" stroke-width="3" stroke-linecap="round"/></svg></div></div>
  <div class="abs social primary" style="left:850px" aria-label="Social profile"></div>
  <div class="abs social" style="left:933px" aria-label="Social profile"></div>
  <div class="abs social" style="left:1015px" aria-label="Social profile"></div>
  <div class="abs safe"><span>Safe Payments</span><span>Safe and Secure SSL Encrypted</span></div>
  <svg class="abs lock" width="30" height="40" viewBox="0 0 30 40"><path d="M8 17v-6a7 7 0 0 1 14 0v6" fill="none" stroke="#111" stroke-width="4"/><rect x="3" y="17" width="24" height="21" rx="2" fill="#111"/></svg>
  <div class="abs payments"><span class="wide"></span><span></span><span></span><span></span><span></span></div>
</footer>
<div class="abs copyright">© 2020 QuillStoneKit, LLC. All Rights are Reserved. Privacy Policy | Site Map | Terms of Service</div>

</body>
</html>
```